Landing Page Design

We need a landing page template designed to support a clients Zenfy Bidpost Campaigns. The client is called Morlet Plumbing and they install and repair hot water systems (only). They provide no other plumbing services.

We are really looking for a great looking landing page that is both engaging and functional.

Target Market(s)

Residential/Domestic market. Typically wives and partners who are typically home or run the household.

Industry/Entity Type

Plumbing

Number of Pages Required

1 page

Requirements
Must have
• Strong branding
Strong call to actions
Great and obvious looking buttons
Nice to have
• Smart use of colour
Should not have
• The design should not use old-style, serif fonts.

Do not include any plumbing images

```html
<!DOCTYPE html>
<html lang="en">
<head>
<meta charset="utf-8">
<title>Morlet Plumbing – Hot Water Solutions</title>
<link rel="stylesheet" href="https://fonts.googleapis.com/css2?family=Arimo:wght@400;700&family=Libre+Baskerville:wght@700&display=swap">
<style>
  :root{
    --page-bg:#f8f8f8;
    --header-bg:#eeeeee;
    --content-bg:#f3f3f3;
    --orange:#f28a1e;
    --orange-dark:#ee7a12;
    --red-orange:#f15a1f;
    --footer:#e8531a;
    --heading-grey:#6b6b6b;
    --text:#111111;
    --input-border:#b5b5b5;
    --white:#ffffff;
  }
  *{box-sizing:border-box;margin:0;padding:0}
  html,body{width:1079px;height:1200px;overflow:hidden}
  body{background:var(--page-bg);font-family:"Arimo",Arial,sans-serif;color:var(--text);position:relative}
  .landing{position:absolute;left:111px;top:109px;width:855px;height:991px;background:var(--content-bg)}
  .site-header{position:absolute;left:0;top:0;width:855px;height:171px;background:var(--header-bg)}
  .brand{position:absolute;left:40px;top:62px;display:flex;align-items:center;gap:10px}
  .brand-mark{width:34px;height:34px;border-radius:50%;background:var(--orange)}
  .brand-name{font-size:30px;font-weight:700;color:var(--red-orange);letter-spacing:.5px}
  .call{position:absolute;right:39px;top:56px;text-align:right;color:var(--orange)}
  .call-label{font-size:18px;display:flex;align-items:center;justify-content:flex-end;gap:3px}
  .call-number{font-size:28px;color:var(--red-orange);margin-top:6px}
  .hero{position:absolute;left:0;top:171px;width:855px;height:151px;overflow:hidden;
    background:radial-gradient(circle at 15% 110%,rgba(255,255,255,.18) 0 30%,transparent 31%),
      radial-gradient(circle at 55% -20%,rgba(255,255,255,.15) 0 35%,transparent 36%),
      linear-gradient(90deg,#fbb634,#fcb21a 60%,#fdbd33)}
  .hero-title{position:absolute;left:0;width:576px;top:22px;text-align:center;font-family:"Libre Baskerville",Georgia,serif;font-size:50px;color:var(--white)}
  .hero-sub{position:absolute;left:0;width:576px;top:94px;text-align:center;font-size:32px;color:var(--white)}
  .hero-points{position:absolute;left:587px;top:12px;list-style:none;font-size:16px;line-height:26px;color:var(--red-orange)}
  .intro-title{position:absolute;left:40px;top:351px;font-size:32px;color:var(--heading-grey);font-weight:400}
  .intro-copy{position:absolute;left:40px;top:408px;width:245px;font-size:13px;line-height:21.6px}
  .intro-copy p+p{margin-top:21.6px}
  .feature-photo{position:absolute;left:301px;top:413px;width:243px;height:452px;background:linear-gradient(160deg,#e9e9e9,#8e8e8e 45%,#c9a48c 80%,#e0c2ae)}
  .btn{position:absolute;left:40px;height:44px;border-radius:3px;background:linear-gradient(#f8a03a,var(--orange-dark));color:var(--white);font-size:17px;letter-spacing:.5px;display:flex;align-items:center;text-decoration:none}
  .btn svg{margin:0 16px 0 22px}
  .btn-quote{top:763px;width:239px}
  .btn-site{top:822px;width:239px}
  .btn-rebates{top:878px;width:504px;justify-content:center}
  .offer{position:absolute;left:587px;top:352px;width:215px;font-size:15px;line-height:16px;letter-spacing:.3px}
  .offer em{font-style:normal;color:var(--red-orange)}
  .field-label{position:absolute;left:587px;font-size:10px;letter-spacing:.3px}
  .field-label span{color:var(--red-orange)}
  .field{position:absolute;left:587px;width:213px;height:22px;background:var(--content-bg);border:1px solid #d8d8d8;border-top-color:var(--input-border);border-left-color:var(--input-border);box-shadow:inset 1px 1px 1px rgba(0,0,0,.15)}
  .field-area{height:112px}
  .btn-enquire{position:absolute;left:587px;top:880px;width:213px;height:43px;border-radius:3px;background:linear-gradient(#f4f4f4,#d9d9d9);border:1px solid #d0d0d0;display:flex;align-items:center;color:var(--orange);font-size:17px;letter-spacing:.8px}
  .btn-enquire svg{margin:0 14px 0 16px}
  .site-footer{position:absolute;left:0;top:970px;width:855px;height:21px;background:var(--footer);color:var(--white);font-size:10px;letter-spacing:.4px;display:flex;align-items:center;padding:0 8px}
  .footer-links{margin-left:auto;display:flex;gap:15px}
  .footer-links a{color:var(--white)}
</style>
</head>
<body>
<div class="landing">
  <header class="site-header">
    <div class="brand"><span class="brand-mark"></span><span class="brand-name">MORLET</span></div>
    <div class="call">
      <div class="call-label">
        <svg width="18" height="18" viewBox="0 0 24 24"><path d="M6.6 10.8a15 15 0 0 0 6.6 6.6l2.2-2.2c.3-.3.7-.4 1-.2 1.1.4 2.3.6 3.6.6.6 0 1 .4 1 1V20c0 .6-.4 1-1 1A17 17 0 0 1 3 4c0-.6.4-1 1-1h3.5c.6 0 1 .4 1 1 0 1.3.2 2.5.6 3.6.1.3 0 .7-.2 1z" fill="#e02a1e"/></svg>
        Call NOW on
      </div>
      <div class="call-number">9741 5208</div>
    </div>
  </header>

  <section class="hero">
    <h1 class="hero-title">Hot water now!</h1>
    <div class="hero-sub">SAVE $$$</div>
    <ul class="hero-points">
      <li>Sydney 24 Hours 7 Days</li>
      <li>On Time</li>
      <li>Professional Technicians</li>
      <li>We Advise on Rebates</li>
      <li>Authorised Halvane Dealer</li>
    </ul>
  </section>

  <h2 class="intro-title">Solar Hot Water Systems</h2>
  <div class="intro-copy">
    <p>Engage our routine office cleaning for at least 6 months and receive a FREE Carpet and Window clean! No strings attached, no contracts.</p>
    <p>To take advantage of this great offer call us on 1300 58 71 40 or complete and submit the form on this page.</p>
    <p>At Tidyra we provide all your property service needs - painlessly. We understand that cleaning and other property services should be background activities. A set and forget proposition.</p>
  </div>

  <div class="feature-photo" role="img" aria-label="Photo of a person enjoying a warm shower"></div>

  <a class="btn btn-quote" href="#">
    <svg width="24" height="26" viewBox="0 0 24 26"><path d="M4 1h11l6 6v18H4z" fill="none" stroke="#fff" stroke-width="2"/><path d="M15 1v6h6" fill="none" stroke="#fff" stroke-width="2"/></svg>
    Book a FREE Quote
  </a>
  <a class="btn btn-site" href="#">
    <svg width="26" height="26" viewBox="0 0 26 26" fill="none" stroke="#fff" stroke-width="1.6"><circle cx="13" cy="13" r="11"/><ellipse cx="13" cy="13" rx="5" ry="11"/><path d="M2 13h22M4 7h18M4 19h18"/></svg>
    Visit Our Web Site
  </a>
  <a class="btn btn-rebates" href="#">Click here for information on Rebates</a>

  <p class="offer">Take advantage of this great offer. Contact Us <em>NOW</em> on <em>9741 5208</em> or register your interest below</p>

  <label class="field-label" style="top:448px">Your First Name: <span>*</span></label>
  <div class="field" style="top:459px"></div>
  <label class="field-label" style="top:502px">Your Surname: <span>*</span></label>
  <div class="field" style="top:514px"></div>
  <label class="field-label" style="top:561px">Your Suburb: <span>*</span></label>
  <div class="field" style="top:573px"></div>
  <label class="field-label" style="top:616px">Best Contact Number: <span>*</span></label>
  <div class="field" style="top:628px"></div>
  <label class="field-label" style="top:671px">Your Email Address: <span>*</span></label>
  <div class="field" style="top:683px"></div>
  <label class="field-label" style="top:724px">Enquiry / Comments: <span>*</span></label>
  <div class="field field-area" style="top:736px"></div>

  <div class="btn-enquire">
    <svg width="30" height="20" viewBox="0 0 30 20" fill="none" stroke="#666" stroke-width="1.6"><path d="M2 7h10l-2-5 12 5h6M22 7v10H10l-8-2V7"/><path d="M14 11h8M14 14h8"/></svg>
    ENQUIRE NOW
  </div>

  <footer class="site-footer">
    <span>MORLET PLUMBING | HOT WATER SOLUTIONS</span>
    <nav class="footer-links">
      <a href="#">INFORMATION ON REBATES</a>
      <a href="#">BOOK A FREE QUOTE</a>
      <a href="#">VISIT OUR WEB SITE NOW</a>
    </nav>
  </footer>
</div>
</body>
</html>
```